FenderPals Personal Injury Lawyers Website (Wordpress)

We need a brand new website for our firm's new rebranding. The name of the website is www.fenderpals-example.com. Our new brand will be a group of personal injury lawyers focused on representing only victims in car wrecks. We will be distinguishing ourselves from other law firms due to the fact that other law firms represent clients involving all forms of personal injury. We will only focus on car wrecks and this needs to be reflected on the website.

I have attached the new firm logo and stationary to show the designers the kind of look we are going for in the new website. It needs to be clean, pure, and show the potential clients that we only do one thing and we do it well. That thing is car wrecks.

Some examples of websites that we like are the following:
www.qvt-example.lu - nice interface and colors. nice navigation, we really like the biography pages for the individuals attorneys
www.morvantlegal-example.com - good layout, good navigation
www.pelliardwoss-example.com - navigation bar follows the user whether the user goes up or down

We would like five separate pages -- (1) Home, (2) Client Resources, (3) Expertise / Car Wrecks, (4) Contact Us, (5) News

The Home page will be used for driving traffic and should have a call to action on the right at the top stating that we will send an ebook to anyone who gives their contact information. The ebook will explain how car wrecks work. This should also have room for youtube videos which will be added later.

The client resources will include blogs, books, and information for potential clients. It should be presented in a well developed manner which is both appealing to potential and current clients.

The expertise page will show that we only focus on car wrecks. This needs to be a recurrent theme throughout the entire website. This page will focus on car wrecks and the different aspects including damages, insurance, and investigation.

The Contact Us page will show a google map to our address and phone number. Please use generic information and we will fill in the gaps upon the selection.

News: the news page will show different articles related to past and present cases and the successes of those clients.

The overall page should be elegant and creative. Do not include courthouses, gavels or anything else related to the law. If you include these things, your design will automatically be excluded.
Updates

Please take note this design is now guaranteed. I look forward to receiving everyone's wonderful designs.

Target Market(s)

Persons involved in car wrecks

Industry/Entity Type

Legal

Coding

Coded - Design and coding required

Number of Pages Required

5+ page

Font styles to use
Serif
Sans Serif

Colors
ec1f27
ffffff
000000

Requirements
Must have
• Five pages which focus on representation of car wreck victims. The site must be clean and easy to navigate.
Nice to have
• Navigation bar should follow user up and down the page.
Should not have
• Gavels, court houses, anything related to the law. If your design has these aspects, it will automatically be rejected

```html
<!DOCTYPE html>
<html lang="en">
<head>
<meta charset="utf-8">
<title>FenderPals – Personal Injury Lawyers</title>
<link href="https://fonts.googleapis.com/css2?family=Oswald:wght@400;500;600&family=Open+Sans:wght@400;600;700&display=swap" rel="stylesheet">
<style>
:root{
  --red:#ec1f27;
  --red-dark:#a3141a;
  --red-deep:#6e0d12;
  --white:#ffffff;
  --black:#000000;
  --ink:#2b2b2b;
  --grey:#6b6b6b;
  --grey-light:#d9d9d9;
  --paper:#f4eeee;
  --footer:#1e1e1e;
}
*{box-sizing:border-box;margin:0;padding:0}
html,body{width:1200px;height:2960px;overflow:hidden}
body{font-family:"Open Sans",Arial,sans-serif;color:var(--ink);background:var(--white);position:relative}
.display{font-family:"Oswald","Arial Narrow",sans-serif;text-transform:uppercase}

/* Hero */
.hero{position:absolute;left:0;top:0;width:1200px;height:600px;overflow:hidden}
.hero-photo{position:absolute;inset:0;background:linear-gradient(100deg,#3a3a3a 0%,#8d8d8d 40%,#c9c9c9 62%,#6e6e6e 100%)}
.topbar{position:absolute;left:0;top:0;width:1200px;height:88px;background:rgba(20,20,20,.55)}
.cta-call{position:absolute;left:16px;top:10px;width:176px;height:26px;background:var(--red);color:var(--white);font-size:11px;font-weight:600;letter-spacing:.5px;display:flex;align-items:center;justify-content:center}
.brand{position:absolute;left:440px;top:0;width:320px;height:120px;background:var(--white);text-align:center;padding-top:8px;z-index:3}
.brand-name{font-family:"Oswald",sans-serif;font-weight:600;font-size:46px;color:var(--red);line-height:1;letter-spacing:1px}
.brand-tag{font-size:11px;letter-spacing:2px;color:var(--grey);margin-top:4px}
.social{position:absolute;left:800px;top:16px;display:flex;gap:8px}
.social span{width:18px;height:18px;border-radius:50%;background:var(--grey-light)}
.search{position:absolute;left:912px;top:12px;width:252px;height:26px;background:rgba(255,255,255,.9);font-size:11px;color:var(--grey);padding:5px 10px}
.nav{position:absolute;left:0;top:88px;width:1200px;height:32px;background:rgba(10,10,10,.75)}
.nav a{position:absolute;top:8px;color:var(--white);text-decoration:none;font-size:12px;font-weight:600;letter-spacing:.5px}
.dropdown{position:absolute;left:208px;top:120px;width:232px;background:var(--white);padding:14px 0;z-index:2;box-shadow:0 4px 10px rgba(0,0,0,.2)}
.dropdown h4{font-size:13px;font-weight:600;color:var(--ink);padding:6px 18px;border-left:3px solid var(--red)}
.dropdown ul{list-style:none;padding:2px 0 10px 30px}
.dropdown li{font-size:11px;color:var(--grey);line-height:18px}
.hero-copy{position:absolute;right:80px;top:140px;text-align:right}
.hero-copy .l1{font-size:58px;color:var(--white);line-height:1.05}
.hero-copy .l2{font-size:58px;color:var(--red);line-height:1.05}
.hero-copy .sub{font-family:"Open Sans",sans-serif;text-transform:none;font-size:15px;color:var(--white);margin-top:10px}
.hero-btn{position:absolute;left:912px;top:300px;width:208px;height:30px;background:var(--red);color:var(--white);font-size:12px;font-weight:600;display:flex;align-items:center;justify-content:center}
.dots{position:absolute;left:544px;top:516px;display:flex;gap:12px}
.dots span{width:14px;height:14px;border-radius:50%;background:rgba(255,255,255,.6)}
.dots span.on{background:var(--red)}
.corner{position:absolute;left:1088px;top:500px;width:112px;height:100px;background:var(--red)}

/* Ebooks */
.ebooks{position:absolute;left:0;top:600px;width:1200px;height:560px;background:radial-gradient(ellipse at 50% 40%,#e8353c 0%,var(--red-dark) 75%)}
.ebooks h2{position:absolute;top:34px;width:100%;text-align:center;font-size:40px;color:var(--white);font-weight:500}
.ebook-cover{position:absolute;left:300px;top:88px;width:300px;height:360px;background:linear-gradient(160deg,#f2f2f2,#9fb6cf)}
.form{position:absolute;left:648px;top:210px;width:352px}
.field{height:32px;background:rgba(255,255,255,.25);border:1px solid rgba(255,255,255,.6);color:var(--white);font-size:11px;font-weight:600;padding:8px 12px;margin-bottom:16px}
.book-btn{position:absolute;left:680px;top:388px;width:288px;height:44px;background:var(--red);border:2px solid var(--white);color:var(--white);font-size:22px;display:flex;align-items:center;justify-content:center;font-family:"Oswald",sans-serif;text-transform:uppercase}

/* About */
.about{position:absolute;left:0;top:1160px;width:1200px;height:680px;background:linear-gradient(180deg,#faf6f6,var(--paper))}
.about h2{position:absolute;top:36px;width:100%;text-align:center;font-size:40px;color:var(--red);font-weight:500}
.about-intro{position:absolute;left:100px;top:96px;width:1000px;text-align:center;font-size:13px;line-height:20px;color:var(--grey)}
.feature{position:absolute;top:170px;width:240px;text-align:center}
.feature h3{font-size:28px;line-height:30px;color:var(--ink);font-weight:500;height:64px}
.feature.accent h3{color:var(--red)}
.feature-pic{width:124px;height:124px;border-radius:50%;margin:10px auto 0;border:4px solid var(--white);box-shadow:0 2px 8px rgba(0,0,0,.2)}
.feature p{font-size:11px;line-height:17px;color:var(--grey);margin-top:40px}
.features-btn{position:absolute;left:528px;top:520px;width:144px;height:36px;background:var(--red);color:var(--white);font-size:13px;font-weight:600;display:flex;align-items:center;justify-content:center}

/* Video */
.video{position:absolute;left:0;top:1840px;width:1200px;height:520px;background:linear-gradient(120deg,var(--red-deep),var(--red) 45%,var(--red-dark))}
.video-title{position:absolute;left:120px;top:24px;color:var(--white)}
.video-title h2{font-size:38px;font-weight:500;line-height:1}
.video-title p{font-size:14px;font-weight:600;margin-top:4px}
.player{position:absolute;left:120px;top:116px;width:620px;height:330px;background:var(--black);border:6px solid #2b2b2b}
.latest{position:absolute;left:860px;top:20px;width:308px;height:480px;background:rgba(0,0,0,.55);padding:16px}
.latest h3{font-size:18px;color:var(--white);font-weight:400;border-bottom:1px solid rgba(255,255,255,.3);padding-bottom:8px}
.item{display:flex;gap:12px;margin-top:18px}
.thumb{width:72px;height:56px;flex:none;background:linear-gradient(135deg,#777,#333)}
.item p{font-size:11px;line-height:15px;color:var(--white)}
.viewall{margin-top:22px;width:76px;height:20px;background:var(--white);color:var(--red);font-size:10px;font-weight:700;display:flex;align-items:center;justify-content:center}

/* Contact */
.contact{position:absolute;left:0;top:2360px;width:1200px;height:240px;background:var(--white)}
.contact h2{position:absolute;top:26px;width:100%;text-align:center;font-size:34px;color:var(--ink);font-weight:500}
.contact-intro{position:absolute;top:76px;width:100%;text-align:center;font-size:12px;color:var(--grey)}
.col{position:absolute;top:120px;font-size:12px;line-height:21px;color:var(--grey)}
.col h4{font-family:"Oswald",sans-serif;font-size:18px;line-height:25px;color:var(--ink);font-weight:500;text-transform:uppercase}
.col b{color:var(--red);font-weight:400}
.col.offset{top:145px}
.map{position:absolute;left:0;top:2600px;width:1200px;height:280px;background:linear-gradient(160deg,#ece7dc,#dcd8cc)}
.footer{position:absolute;left:0;top:2880px;width:1200px;height:80px;background:var(--footer);color:#bbb;font-size:12px;display:flex;align-items:center;justify-content:center;padding-top:10px}
.to-top{position:absolute;left:576px;top:2856px;width:48px;height:48px;border-radius:50%;background:var(--red)}
</style>
</head>
<body>

<header class="hero">
  <div class="hero-photo" role="img" aria-label="Photo of a wrecked car after a collision"></div>
  <div class="topbar">
    <div class="cta-call">REQUEST CALL TO ACTION</div>
    <div class="social"><span></span><span></span><span></span><span></span></div>
    <div class="search">SEARCH</div>
  </div>
  <div class="brand">
    <div class="brand-name">FENDERPALS</div>
    <div class="brand-tag">PERSONAL INJURY LAWYERS</div>
  </div>
  <nav class="nav">
    <a style="left:232px">HOME</a>
    <a style="left:316px">CLIENT RESOURCES</a>
    <a style="left:776px">EXPERTISE / CAR WRECKS</a>
    <a style="left:960px">CONTACT US</a>
    <a style="left:1080px">NEWS</a>
  </nav>
  <div class="dropdown">
    <h4>Heading 1</h4>
    <ul><li>Sub Heading 1</li><li>Sub Heading 2</li></ul>
    <h4>Heading 2</h4>
    <ul><li>Sub Heading 1</li><li>Sub Heading 2</li><li>Sub Heading 3</li></ul>
    <h4>Heading 3</h4>
  </div>
  <div class="hero-copy display">
    <div class="l1">When it comes to defence</div>
    <div class="l2">The gloves are off</div>
    <div class="sub">Our Dedicated Team Fights For The Best Outcomes</div>
  </div>
  <div class="hero-btn">FREE CONSULTATION</div>
  <div class="dots"><span></span><span class="on"></span><span></span><span></span></div>
  <div class="corner"></div>
</header>

<section class="ebooks">
  <h2 class="display">Free eBooks</h2>
  <div class="ebook-cover" role="img" aria-label="Ebook cover: After an auto accident, steps to take and pitfalls to avoid"></div>
  <div class="form">
    <div class="field">FIRST NAME</div>
    <div class="field">EMAIL ADDRESS</div>
    <div class="field">PHONE NUMBER</div>
  </div>
  <div class="book-btn">Get your book now</div>
</section>

<section class="about">
  <h2 class="display">About Us</h2>
  <p class="about-intro">We focus on one thing only: car wrecks. Our lawyers stand beside drivers, passengers and families from the first call to the final settlement. We gather the evidence, handle the insurers and explain every step in plain language, so you can focus on healing while we fight for the full recovery you deserve after a crash on the road.</p>
  <div class="feature" style="left:180px">
    <h3 class="display">Team</h3>
    <div class="feature-pic" style="background:linear-gradient(135deg,#555,#1c1c1c)" role="img" aria-label="Team icon"></div>
    <p>Experienced car wreck lawyers who know how insurers think and how to build a strong claim for you.</p>
  </div>
  <div class="feature" style="left:480px">
    <h3 class="display">Service we provide</h3>
    <div class="feature-pic" style="background:linear-gradient(135deg,#aaa,#666)" role="img" aria-label="Service icon"></div>
    <p>Crash investigation, damages review and insurance negotiation, all handled under one roof for every client.</p>
  </div>
  <div class="feature accent" style="left:780px">
    <h3 class="display">Customer support</h3>
    <div class="feature-pic" style="background:linear-gradient(135deg,#f0555b,var(--red-dark))" role="img" aria-label="Customer support icon"></div>
    <p>Reach us any day of the week for updates on your case, answers to questions and honest advice.</p>
  </div>
  <div class="features-btn">View All Features</div>
</section>

<section class="video">
  <div class="video-title display">
    <h2>Carwreck Video 1</h2>
    <p>Information about video</p>
  </div>
  <div class="player">
    <svg width="608" height="318" viewBox="0 0 608 318"><circle cx="304" cy="159" r="28" fill="none" stroke="#ec1f27" stroke-width="3"/><path d="M295 145 L318 159 L295 173 Z" fill="#ec1f27"/></svg>
  </div>
  <aside class="latest">
    <h3 class="display">Latest Video</h3>
    <div class="item"><div class="thumb" role="img" aria-label="Video thumbnail"></div><p>What to do in the first hour after a crash on the highway</p></div>
    <div class="item"><div class="thumb" role="img" aria-label="Video thumbnail"></div><p>How insurers value your claim and what you can do about it</p></div>
    <div class="item"><div class="thumb" role="img" aria-label="Video thumbnail"></div><p>Gathering photos and witness notes at the scene of a wreck</p></div>
    <div class="item"><div class="thumb" role="img" aria-label="Video thumbnail"></div><p>Client story: a full recovery after a rear end collision</p></div>
    <div class="viewall">VIEW ALL</div>
  </aside>
</section>

<section class="contact">
  <h2 class="display">Contact Us</h2>
  <p class="contact-intro">Call, write or stop by the office for a free review of your car wreck case.</p>
  <div class="col" style="left:220px"><h4>Address</h4>123 Street Name, S. 321<br>City Name, State Name</div>
  <div class="col offset" style="left:480px">Tel: <b>(123) 456-7890</b><br>Fax: <b>(123) 987-6543</b><br>Email: <b>hello@fenderpals-example.com</b></div>
  <div class="col offset" style="left:780px">Web: <b>www.fenderpals-example.com</b><br>News: <b>fenderpals-example.com/news</b><br>Blog: <b>fenderpals-example.com/blog</b></div>
</section>

<div class="map" role="img" aria-label="Street map showing the office location"></div>

<footer class="footer">© FenderPals Law Group. All Rights Reserved</footer>
<div class="to-top"><svg width="48" height="48" viewBox="0 0 48 48"><path d="M16 28 L24 20 L32 28" fill="none" stroke="#fff" stroke-width="3"/></svg></div>

</body>
</html>
```